New Advertising Company Business Card

A two sided business card. One side with logo only and the other side with my information and maybe my logo again. Looking for something unique and creative, but not too busy. Info would include my name(Marcus Feldon), President, phone number, address, email address, and website. LOGO IS THE BLUE AND WHITE ONE.

Target Market(s)

CEO/VP Level Audience

Industry/Entity Type

Business

Contact Information for Business Card

In Description.

```html
<!DOCTYPE html>
<html lang="en">
<head>
<meta charset="utf-8">
<title>Meridian Advertising – Business Card</title>
<link rel="stylesheet" href="https://fonts.googleapis.com/css2?family=Work+Sans:wght@400;600;700&display=swap">
<style>
  :root {
    --backdrop: #1b1b1b;
    --card: #262626;
    --card-edge: #2e2e2e;
    --brand-blue: #1f78c8;
    --ink-white: #f2f2f2;
    --ink-soft: #d9d9d9;
  }
  * { box-sizing: border-box; margin: 0; padding: 0; }
  html, body {
    width: 1200px; height: 900px; overflow: hidden;
    background: var(--backdrop);
    font-family: "Work Sans", Arial, sans-serif;
  }
  .canvas {
    position: relative; width: 1200px; height: 900px;
    display: flex; flex-direction: column; align-items: center;
    justify-content: center; gap: 44px;
  }
  .card {
    position: relative; width: 700px; height: 400px;
    background: linear-gradient(135deg, var(--card) 0%, var(--card-edge) 100%);
    box-shadow: 0 18px 40px rgba(0,0,0,.55);
    overflow: hidden;
  }
  .card__band {
    position: absolute; left: 0; right: 0; bottom: 0; height: 10px;
    background: var(--brand-blue);
  }
  .wordmark {
    display: flex; align-items: center; gap: 14px;
    font-weight: 700; color: var(--ink-white);
    letter-spacing: .08em; text-transform: uppercase; line-height: 1.05;
  }
  .wordmark__dot {
    width: 22px; height: 22px; border-radius: 50%;
    background: var(--brand-blue); flex: none;
  }
  .card--front .wordmark {
    position: absolute; left: 50%; top: 150px; transform: translateX(-50%);
    font-size: 46px; white-space: nowrap;
  }
  .card--front .web {
    position: absolute; left: 0; right: 0; bottom: 46px; text-align: center;
    font-size: 17px; letter-spacing: .12em; color: var(--ink-white);
  }
  .web__name { color: var(--brand-blue); }

  .card--back .wordmark {
    position: absolute; left: 44px; top: 150px; font-size: 30px;
    flex-direction: row;
  }
  .wordmark__stack { display: flex; flex-direction: column; }
  .divider {
    position: absolute; left: 372px; top: 80px; width: 2px; height: 220px;
    background: var(--brand-blue);
  }
  .details { position: absolute; left: 402px; top: 82px; color: var(--ink-soft); }
  .details__name {
    font-size: 26px; font-weight: 700; color: var(--brand-blue);
    letter-spacing: .05em; text-transform: uppercase;
  }
  .details__title { font-size: 18px; margin-top: 2px; color: var(--ink-white); }
  .details__address { font-size: 17px; margin-top: 18px; line-height: 1.3; letter-spacing: .03em; }
  .contact { list-style: none; margin-top: 16px; font-size: 17px; letter-spacing: .03em; }
  .contact li { display: flex; align-items: center; gap: 12px; margin-bottom: 6px; }
  .contact svg { width: 16px; height: 16px; fill: var(--brand-blue); flex: none; }
</style>
</head>
<body>
<main class="canvas">
  <section class="card card--front" aria-label="Card front">
    <div class="wordmark"><span class="wordmark__dot"></span><span>Meridian Advertising</span></div>
    <p class="web">www.<span class="web__name">lumenpartners</span>.com</p>
    <div class="card__band"></div>
  </section>

  <section class="card card--back" aria-label="Card back">
    <div class="wordmark">
      <span class="wordmark__dot"></span>
      <span class="wordmark__stack"><span>Meridian</span><span>Advertising</span></span>
    </div>
    <div class="divider"></div>
    <div class="details">
      <h1 class="details__name">Marcus Feldon</h1>
      <p class="details__title">President</p>
      <p class="details__address">418 Cedar Ridge Drive<br>Dallas, TX 75201</p>
      <ul class="contact">
        <li>
          <svg viewBox="0 0 24 24" aria-hidden="true"><path d="M6.6 10.8a15.1 15.1 0 0 0 6.6 6.6l2.2-2.2a1 1 0 0 1 1-.25 11.4 11.4 0 0 0 3.6.57 1 1 0 0 1 1 1V20a1 1 0 0 1-1 1A17 17 0 0 1 3 4a1 1 0 0 1 1-1h3.5a1 1 0 0 1 1 1c0 1.25.2 2.45.57 3.57a1 1 0 0 1-.25 1z"/></svg>
          <span>555 214 0387</span>
        </li>
        <li>
          <svg viewBox="0 0 24 24" aria-hidden="true"><path d="M2 5h20v14H2zm2 2v.5l8 5 8-5V7l-8 5z"/></svg>
          <span>info@LumenPartners.com</span>
        </li>
        <li>
          <svg viewBox="0 0 24 24" aria-hidden="true"><path d="M12 2a10 10 0 1 0 0 20 10 10 0 0 0 0-20zm0 2c.9 1.2 1.6 2.6 2 4h-4c.4-1.4 1.1-2.8 2-4zM4.3 14a8 8 0 0 1 0-4h3.4a16 16 0 0 0 0 4zm.9 2h3a14 14 0 0 0 1.3 3.6A8 8 0 0 1 5.2 16zm3-8h-3a8 8 0 0 1 4.3-3.6A14 14 0 0 0 8.2 8zM12 20c-.9-1.2-1.6-2.6-2-4h4c-.4 1.4-1.1 2.8-2 4zm2.3-6H9.7a14 14 0 0 1 0-4h4.6a14 14 0 0 1 0 4zm.2 5.6A14 14 0 0 0 15.8 16h3a8 8 0 0 1-4.3 3.6zM16.3 14a16 16 0 0 0 0-4h3.4a8 8 0 0 1 0 4zm-.5-6a14 14 0 0 0-1.3-3.6A8 8 0 0 1 18.8 8z"/></svg>
          <span>www.<span class="web__name">lumenpartners</span>.com</span>
        </li>
      </ul>
    </div>
    <div class="card__band"></div>
  </section>
</main>
</body>
</html>
```